Business Card design for construction company

I would like a business card design for a construction company - Harlow Constructions. I have attached the ai logo file for use. I would like the card to be very smart and clean and incorporate only white and the two colours in the logo. I would like the card to have two sides. One side can just have the logo, the other with the relevant information.

Target Market(s)

Building and Construction Clients

Industry/Entity Type

Business

Contact Information for Business Card

Name: Tom Pardoe
Company: Harlow Constructions Pty Limited
Address: 14 Mallee Crescent Carrow Vale 2093
Phone: 0427 531 068
Email: tomp@harlowbuild-example.com.au

Font styles to use
Serif
Sans Serif

Requirements
Must have
• Details noted above
• Logo as provided
• Colours as in logo
• Square edges
• A font that compliments the logo
Should not have
• Any colour other than white and those in logo
• Rounded edges

```html
<!DOCTYPE html>
<html lang="en">
<head>
<meta charset="utf-8">
<title>Harlow Constructions – Business Card</title>
<link href="https://fonts.googleapis.com/css2?family=Arimo:wght@400;700&display=swap" rel="stylesheet">
<style>
  :root {
    --brand-blue: #14ace8;
    --brand-charcoal: #454a4f;
    --paper: #ffffff;
    --backdrop: #e9ebed;
    --rule: #8c9095;
    --ink: #3b3f44;
  }
  * { box-sizing: border-box; margin: 0; padding: 0; }
  html, body {
    width: 1200px; height: 900px; overflow: hidden;
    background: var(--backdrop);
    font-family: "Arimo", Arial, sans-serif;
    color: var(--ink);
  }
  .card {
    position: absolute;
    left: 280px;
    width: 640px; height: 366px;
    box-shadow: 0 10px 28px rgba(0,0,0,0.18);
  }
  .card--front { top: 52px; background: var(--brand-blue); display: flex; align-items: center; justify-content: center; }
  .card--back { top: 482px; background: var(--paper); overflow: hidden; }

  .wordmark {
    font-weight: 400;
    text-transform: uppercase;
    letter-spacing: 0.16em;
    white-space: nowrap;
  }
  .card--front .wordmark { color: var(--paper); font-size: 34px; }
  .card--back .wordmark {
    position: absolute; left: 62px; top: 56px;
    color: var(--brand-charcoal); font-size: 26px;
  }

  .edge-band { position: absolute; left: 0; top: 0; width: 24px; height: 366px; }

  .address {
    position: absolute; right: 40px; top: 132px;
    text-align: right; font-size: 14px; line-height: 1.35;
  }
  .rule { position: absolute; height: 1px; background: var(--rule); }
  .rule--long { left: 250px; right: 34px; top: 186px; }
  .rule--short { left: 62px; width: 250px; top: 268px; }

  .person { position: absolute; left: 62px; top: 196px; }
  .person__name { color: var(--brand-blue); font-weight: 700; font-size: 28px; letter-spacing: -0.01em; }
  .person__role { font-size: 16px; margin-top: 2px; }

  .contacts { position: absolute; left: 62px; top: 280px; list-style: none; font-size: 14px; }
  .contacts li { display: flex; align-items: center; gap: 8px; height: 21px; }
  .contacts svg { width: 13px; height: 13px; fill: var(--brand-blue); flex: none; }
</style>
</head>
<body>

<section class="card card--front" aria-label="Card front">
  <span class="wordmark">Harlow Constructions</span>
</section>

<section class="card card--back" aria-label="Card back">
  <svg class="edge-band" viewBox="0 0 24 366" aria-hidden="true">
    <rect x="0" y="0" width="24" height="366" fill="var(--brand-charcoal)"/>
    <polygon points="0,0 24,0 24,172 0,156" fill="var(--brand-blue)"/>
  </svg>

  <span class="wordmark">Harlow Constructions</span>

  <address class="address" style="font-style:normal">
    14 Mallee Crescent<br>Carrow Vale 2093
  </address>

  <div class="rule rule--long"></div>

  <div class="person">
    <div class="person__name">Tom Pardoe</div>
    <div class="person__role">President</div>
  </div>

  <div class="rule rule--short"></div>

  <ul class="contacts">
    <li>
      <svg viewBox="0 0 16 16" aria-hidden="true"><path d="M3.6 1.2l2.3 2.6-1.3 1.9c.9 2 2.5 3.6 4.5 4.6l1.9-1.3 2.6 2.3-1.2 2.4C7 13.7 2.3 9 1.2 3.6z"/></svg>
      0427 531 068
    </li>
    <li>
      <svg viewBox="0 0 16 16" aria-hidden="true"><path d="M1 3h14v1.2L8 9 1 4.2z M1 5.8l7 4.7 7-4.7V13H1z"/></svg>
      tomp@harlowbuild-example.com.au
    </li>
    <li>
      <svg viewBox="0 0 16 16" aria-hidden="true"><path d="M8 1a7 7 0 100 14A7 7 0 008 1zm0 1.3c.8 0 1.7 1.4 2 3.7H6c.3-2.3 1.2-3.7 2-3.7zM2.4 7h2.5v2H2.4a5.7 5.7 0 010-2zm3.6 0h4v2H6zm5.1 0h2.5a5.7 5.7 0 010 2h-2.5zM6 10h4c-.3 2.3-1.2 3.7-2 3.7S6.3 12.3 6 10z"/></svg>
      www.harlowbuild-example.com.au
    </li>
  </ul>
</section>

</body>
</html>
```